Corporate Web Redesign Project - coded

We would like redesign/refresh of our current site that would allow us to increase the depth of content and create a high quality impression for visitors.

Current site - http://corvanisystems.com/

A previous web redesign project has improved our site but it has not really reached the level we require.

Our customers are global, blue chip, organisations and a professional, corporate style of site is required.

Please note we would prefer a coded website to a just a design. We are happy to provide a zip of our current site if required.
Updates

                                   

Target Market(s)

Global oil and gas producers, KR, Tamberline, Orvadex etc.

Industry/Entity Type

It Professional

Requirements
Must have
• Design should support the level of content we currently have in the existing sitemap - although it should be expandable a site design for a large / complex site would not be appropriate

All current content / pages to be reflected in design

Must be visually appealing

Intuitive and clear navigation that is expandable

Display a high level of professionalism

Use a consistent palette of colours that complements our logo

Clean and organized layout

A way to capture visitor’s information or Call to action (i.e. contact link or form) on every page

Prominent Contact Information
Should not have
• Flash

```html
<!DOCTYPE html>
<html lang="en">
<head>
<meta charset="utf-8">
<title>Corvani Systems – QTX Probabilistic Time &amp; Cost Software</title>
<link rel="stylesheet" href="https://fonts.googleapis.com/css2?family=Open+Sans:wght@400;600;700&display=swap">
<style>
:root{
  --teal:#1f4b5b;
  --teal-dark:#173c49;
  --olive:#3e4a1c;
  --olive-dot:#5d6b2a;
  --text:#3a3a3a;
  --muted:#555;
  --line:#dcdcdc;
  --panel:#f6f6f6;
  --footer:#232323;
  --white:#fff;
}
*{box-sizing:border-box;margin:0;padding:0}
html,body{width:1140px;height:1200px;overflow:hidden}
body{position:relative;background:var(--white);font-family:"Open Sans",Arial,sans-serif;color:var(--text)}
.hero{position:absolute;left:0;top:0;width:1140px;height:370px;
  background:linear-gradient(180deg,#e9eef3 0%,#dfe6ee 35%,#c9d3de 65%,#9aa7b6 88%,#8a8680 100%)}
.hero-band{position:absolute;left:0;top:370px;width:1140px;height:5px;background:#c4c4c4}
.site-header{position:absolute;left:95px;top:18px;width:950px;height:78px;background:var(--white);border-bottom:1px solid #9a9a9a}
.brand{position:absolute;left:12px;top:24px;display:flex;align-items:center;gap:8px;font-weight:700;font-size:19px;color:var(--teal)}
.brand-mark{width:22px;height:22px;border-radius:50%;background:var(--teal)}
.main-nav{position:absolute;right:20px;top:30px;display:flex;gap:38px;font-size:14px;color:var(--teal)}
.hero-title{position:absolute;left:96px;top:198px;font-size:29px;line-height:37px;font-weight:700;color:#111;letter-spacing:.3px}
.content{position:absolute;left:95px;top:401px;width:662px;height:727px;border:1px solid #e1e1e1;background:var(--white);padding:10px 24px 0 24px;overflow:hidden}
.product-head{display:flex;align-items:baseline;gap:10px;color:var(--teal-dark)}
.product-head b{font-size:41px;font-weight:600}
.product-head span{font-size:19px;color:#222}
.intro p{font-size:12.3px;line-height:20px;color:var(--muted);margin-top:14px;width:620px}
.intro p:first-child{line-height:15px;margin-top:10px}
.divider{border:0;border-top:1px solid var(--line);margin:27px -5px 0 -5px}
.features-title{text-align:center;font-size:29px;font-weight:600;color:var(--teal);margin-top:24px;letter-spacing:.5px;padding-right:40px}
.features{display:grid;grid-template-columns:353px 270px;row-gap:22px;margin-top:24px;margin-left:-4px}
.feature{display:flex;gap:14px}
.feature svg{flex:none;width:40px;height:36px}
.feature h3{font-size:20px;font-weight:600;color:#222;line-height:22px}
.feature ul{list-style:none;margin-top:6px}
.feature li{position:relative;padding-left:17px;font-size:12.3px;line-height:14.5px;color:var(--muted);margin-bottom:7.3px;max-width:250px}
.feature.right li{max-width:200px}
.feature li::before{content:"";position:absolute;left:2px;top:5px;width:5px;height:5px;border-radius:50%;background:var(--teal)}
.side-box{position:absolute;left:777px;width:262px;background:var(--panel);border:1px solid #e2e2e2;border-radius:3px}
.news{top:401px;height:457px}
.side-box h2{font-size:19px;font-weight:600;color:var(--teal);margin:15px 0 0 11px}
.side-inner{position:absolute;left:10px;right:10px;background:var(--white);border:1px solid #e4e4e4;border-radius:2px}
.news .side-inner{top:52px;height:394px;padding:0 8px 0 13px}
.news-item h4{font-size:13.5px;font-weight:600;color:var(--olive);margin-top:9px;position:relative;padding-left:14px}
.news-item h4::before{content:"";position:absolute;left:1px;top:7px;width:5px;height:5px;border-radius:50%;background:var(--olive-dot)}
.news-item p{font-size:12px;line-height:20px;color:var(--muted);margin-top:7px;padding-left:2px}
.news-item+.news-item{border-top:1px solid #d2d2d2;margin-top:14px;padding-top:6px}
.contact{top:875px;height:254px}
.contact .side-inner{top:47px;height:198px;padding-top:12px}
.field{display:flex;align-items:flex-start;margin-bottom:10px}
.field label{width:74px;text-align:right;padding-right:8px;font-size:11.5px;color:#333;padding-top:4px}
.field .input{width:153px;height:24px;border:1px solid #d6d6d6;font-size:8.5px;font-style:italic;color:#aaa;padding:6px 8px}
.field .input.tall{height:72px}
.submit{position:absolute;right:12px;bottom:8px;background:var(--teal);color:var(--white);font-size:12.5px;padding:3px 10px;border-radius:2px}
.site-footer{position:absolute;left:0;top:1148px;width:1140px;height:52px;background:var(--footer);color:var(--white);font-size:11px;font-weight:600}
.copyright{position:absolute;left:94px;top:19px}
.social{position:absolute;right:94px;top:16px;display:flex;align-items:center;gap:8px}
.social span{margin-right:6px}
.social i{display:block;width:20px;height:20px;border-radius:3px}
</style>
</head>
<body>
<div class="hero" role="img" aria-label="Photograph of a businessman sitting cross-legged with a laptop, arms raised in celebration, against a soft cloudy sky"></div>
<div class="hero-band"></div>

<header class="site-header">
  <div class="brand"><span class="brand-mark"></span>Corvani Systems</div>
  <nav class="main-nav"><span>Home</span><span>News</span><span>About Us</span><span>Solutions</span><span>Technologies</span></nav>
</header>

<h1 class="hero-title">PROBABILISTIC TIME &amp;<br>COST SOFTWARE</h1>

<main class="content">
  <div class="product-head"><b>QTX</b><span>- Probabilistic Time &amp; Cost Software</span></div>
  <div class="intro">
    <p>It can be difficult to account for the risk inherent in drilling operations, create a time and cost estimate then present the AFE in a way that communicates that risk to all project stakeholders</p>
    <p>The standard solution has generally been complex Tabula spreadsheets that are often individual to each engineer. Unfortunately Tabula spreadsheets are prone to error and difficult for other users to share and understand.</p>
    <p>Complex Tabula spreadsheets therefore result in inconsistent and inaccurate estimating within your team.QTX delivers a standardized, systematic approach to understanding and communicating project risk.</p>
    <p>Using QTX Templates you can capture your existing processes and implement a powerful, fast and easy solution for creating probabilistic time and cost estimates.</p>
  </div>
  <hr class="divider">
  <h2 class="features-title">MAIN FEATURES</h2>
  <div class="features">
    <div class="feature">
      <svg viewBox="0 0 40 36" aria-hidden="true"><path d="M4 8h24v-5l8 8-8 8v-5H11v6H4z M36 28H12v5l-8-8 8-8v5h17v-6h7z" fill="#1f4b5b"/></svg>
      <div><h3>Define Process</h3><ul><li>Convert existing Tabula models</li><li>Your company processes</li><li>Consistent, Systematic and Robust</li><li>Define the inputs you want</li><li>Run the reports you need</li></ul></div>
    </div>
    <div class="feature right">
      <svg viewBox="0 0 40 36" aria-hidden="true"><circle cx="20" cy="19" r="13" fill="none" stroke="#1f4b5b" stroke-width="3"/><rect x="15" y="14" width="10" height="10" fill="#1f4b5b"/><circle cx="20" cy="5" r="4" fill="#1f4b5b"/><circle cx="9" cy="27" r="4" fill="#1f4b5b"/><circle cx="31" cy="27" r="4" fill="#1f4b5b"/></svg>
      <div><h3>Develop Estimate</h3><ul><li>Any type or level of estimate</li><li>Offset Data link to generate times</li><li>Cost Model with spread rates, tangibles, and complex costs</li><li>Fast and simple to use</li></ul></div>
    </div>
    <div class="feature">
      <svg viewBox="0 0 40 36" aria-hidden="true"><path d="M26 6H6v26h26V14" fill="none" stroke="#1f4b5b" stroke-width="4"/><path d="M14 24l2-7 16-15 5 5-16 15z" fill="#1f4b5b"/></svg>
      <div><h3>Build Campaign</h3><ul><li>Build a multi-well development</li><li>Multiply single-well concepts</li><li>Add Learning and NPT curves</li><li>Re-order &amp; run scenarios</li><li>Transparent and Auditable estimate</li></ul></div>
    </div>
    <div class="feature right">
      <svg viewBox="0 0 40 36" aria-hidden="true"><circle cx="12" cy="14" r="5" fill="#1f4b5b"/><path d="M2 34c0-8 4-12 10-12s10 4 10 12z" fill="#1f4b5b"/><ellipse cx="29" cy="8" rx="9" ry="6" fill="#1f4b5b"/><path d="M24 12l-3 6 7-4z" fill="#1f4b5b"/><circle cx="24" cy="22" r="3.5" fill="#1f4b5b"/><path d="M18 34c0-6 2-8 6-8s6 2 6 8z" fill="#1f4b5b"/></svg>
      <div><h3>Communicate</h3><ul><li>Custom reporting module</li><li>Configurable Tabula reporting / charting</li><li>Clear and consistent output</li><li>Clearly communicate risk / cost to stakeholders</li></ul></div>
    </div>
  </div>
</main>

<aside class="side-box news">
  <h2>QTX NEWS</h2>
  <div class="side-inner">
    <div class="news-item">
      <h4>Orvadex upgrade to QTX 5.0</h4>
      <p>QTX 5.0 is a major product release incorporating updated multi-well and learning functionality as well as new configuration allowing the Offset Data Mapper to link to various kinds of data sources.</p>
    </div>
    <div class="news-item">
      <h4>100% success rate</h4>
      <p>We are pleased to have been selected in all competitive tenders by a range of international operators including Harrowgate Energy, Veltmark Gas and Orvadex. This reinforces our belief that QTX provides the best solution for wells time and cost estimating in the marketplace.</p>
    </div>
  </div>
</aside>

<aside class="side-box contact">
  <h2>Quick Contact</h2>
  <div class="side-inner">
    <div class="field"><label>Name:</label><div class="input">Please enter your name</div></div>
    <div class="field"><label>Email:</label><div class="input">Please enter your email address</div></div>
    <div class="field"><label>Comments:</label><div class="input tall">Please enter your comments</div></div>
    <div class="submit">Submit</div>
  </div>
</aside>

<footer class="site-footer">
  <div class="copyright">© Copyrights 2013&nbsp; Corvani Systems LTD. All rights Reserved</div>
  <div class="social"><span>Stay Connected:</span><i style="background:#3b5a96"></i><i style="background:#3fa7d8"></i><i style="background:#2a7ab3"></i></div>
</footer>
</body>
</html>
```